Small boutique home based travel agency needs a flyer design and logo

I need a flyer design for my boutique home-based travel agency that specializes in designing personalized trips to Europe, ocean and river cruises and escorted small group tours to exotic destinations.

We are travel experts, provide the best customer service in the industry and would like this promoted. Open by appointment.
Would like the flyer and logo to use a globe and I like color. Please integrate photo.

Boutique

```html
<!DOCTYPE html>
<html lang="en">
<head>
<meta charset="utf-8">
<title>Voyara Travel — Flyer and Card Layouts</title>
<link rel="stylesheet" href="https://fonts.googleapis.com/css2?family=Roboto+Condensed:wght@400;700&family=Open+Sans:wght@400;700&display=swap">
<style>
  :root{
    --stage:#000000;
    --paper:#ffffff;
    --teal:#1c6f6c;
    --sky:#3ec7e6;
    --ocean:#0a7fcf;
    --deep:#0b3f9e;
    --pill:#0e3f86;
    --link:#1aa3d8;
    --label:#ffffff;
    --body:#1d2b3a;
    --globe-rim:#2b97b3;
  }
  *{box-sizing:border-box;margin:0;padding:0}
  html,body{width:1200px;height:874px;overflow:hidden;background:var(--stage)}
  .sheet{position:relative;width:1200px;height:874px;font-family:"Open Sans",Arial,sans-serif}

  .panel{
    position:absolute;overflow:hidden;
    background:linear-gradient(180deg,var(--paper) 0%,var(--paper) 50%,#dff6fb 62%,var(--sky) 76%,var(--ocean) 88%,var(--deep) 100%);
  }
  .panel .waves{position:absolute;left:0;bottom:0;width:100%;height:55%}

  .panel-label{position:absolute;color:var(--label);font:700 10px "Open Sans",Arial,sans-serif;letter-spacing:.2px}

  .brand{position:absolute;display:flex;align-items:center;gap:8px;color:var(--teal);
    font-family:"Roboto Condensed",Arial,sans-serif;font-weight:700;line-height:.95;text-transform:uppercase}
  .brand-mark{flex:none;border-radius:50%;background:var(--teal)}
  .brand-name{display:block}

  .contact{position:absolute;text-align:center;color:var(--paper);font:700 10px "Open Sans",Arial,sans-serif;line-height:15px}
  .contact .pill{display:inline-block;background:var(--pill);border-radius:8px;padding:0 5px;margin:1px 0}
  .contact .web-pill{display:inline-block;background:var(--pill);color:var(--sky);border-radius:8px;padding:0 6px;margin-top:6px}

  .web-strip{position:absolute;left:0;width:100%;height:26px;background:linear-gradient(90deg,#f4f8fb,#dde8f2);
    display:flex;align-items:center}
  .web-strip .web{color:var(--link);font:700 10px "Open Sans",Arial,sans-serif}

  .photo-globe{position:absolute;border-radius:50%;
    background:linear-gradient(145deg,#5a8fa8 0%,#7fb3c9 30%,#4f93b4 55%,#3b7f9c 75%,#2a6f8a 100%);
    box-shadow:inset 0 0 0 12px var(--globe-rim),0 2px 6px rgba(0,0,0,.25)}
  .faint-globe{position:absolute;border-radius:50%;
    background:radial-gradient(circle,rgba(255,255,255,0) 55%,rgba(62,170,222,.35) 72%,rgba(62,170,222,.7) 76%,rgba(255,255,255,0) 80%)}
  .blurb{font:400 6.4px "Open Sans",Arial,sans-serif;color:var(--body);line-height:8px}
</style>
</head>
<body>
<main class="sheet">

  <section class="panel" style="left:32px;top:25px;width:500px;height:385px">
    <svg class="waves" viewBox="0 0 500 210" preserveAspectRatio="none" aria-hidden="true">
      <path d="M0 90 C120 40 260 150 500 70 L500 210 L0 210Z" fill="rgba(255,255,255,.25)"/>
      <path d="M0 140 C150 90 300 180 500 120" stroke="rgba(255,255,255,.6)" stroke-width="3" fill="none"/>
    </svg>
    <div class="photo-globe" role="img" aria-label="Globe-shaped collage of travel photos: European landmarks, map of Europe, cruise ship, coastline and travellers" style="left:178px;top:-15px;width:340px;height:340px"></div>
    <div class="brand" style="left:36px;top:62px;font-size:22px">
      <span class="brand-mark" style="width:14px;height:14px"></span>
      <span class="brand-name">Voyara<br>Travel</span>
    </div>
    <div class="contact" style="left:40px;top:307px;width:90px">555-014-2238<br>hello@voyaratravel.com</div>
    <div class="web-strip" style="top:343px">
      <span class="web" style="margin-left:31px;width:150px">VoyaraTravel.com</span>
      <p class="blurb" style="width:290px">My boutique home-based travel agency specializes in designing personalized trips to Europe, ocean and river cruises and escorted small group tours to exotic destinations.</p>
    </div>
  </section>

  <section class="panel" style="left:553px;top:25px;width:169px;height:391px">
    <svg class="waves" viewBox="0 0 170 210" preserveAspectRatio="none" aria-hidden="true">
      <path d="M0 100 C50 60 110 150 170 90 L170 210 L0 210Z" fill="rgba(255,255,255,.25)"/>
    </svg>
    <div class="brand" style="left:30px;top:75px;font-size:19px">
      <span class="brand-mark" style="width:12px;height:12px"></span>
      <span class="brand-name">Voyara<br>Travel</span>
    </div>
    <div class="contact" style="left:0;top:312px;width:169px">555-014-2238<br>hello@voyaratravel.com</div>
    <div class="web-strip" style="top:347px;justify-content:center"><span class="web">VoyaraTravel.com</span></div>
  </section>
  <p class="panel-label" style="left:553px;top:421px">FRONT</p>

  <section class="panel" style="left:750px;top:25px;width:168px;height:393px">
    <svg class="waves" viewBox="0 0 170 210" preserveAspectRatio="none" aria-hidden="true">
      <path d="M0 100 C50 60 110 150 170 90 L170 210 L0 210Z" fill="rgba(255,255,255,.25)"/>
    </svg>
    <div class="brand" style="left:16px;top:140px;font-size:27px">
      <span class="brand-mark" style="width:14px;height:14px"></span>
      <span class="brand-name">Voyara<br>Travel</span>
    </div>
    <div class="contact" style="left:0;top:312px;width:168px">
      <span class="pill">555-014-2238</span><br><span class="pill">hello@voyaratravel.com</span><br><span class="web-pill">VoyaraTravel.com</span>
    </div>
  </section>
  <p class="panel-label" style="left:750px;top:423px">BACK (OPTION 1)</p>

  <section class="panel" style="left:943px;top:25px;width:178px;height:394px">
    <svg class="waves" viewBox="0 0 170 210" preserveAspectRatio="none" aria-hidden="true">
      <path d="M0 100 C50 60 110 150 170 90 L170 210 L0 210Z" fill="rgba(255,255,255,.25)"/>
    </svg>
    <div class="faint-globe" role="img" aria-label="Faint wireframe globe decoration" style="left:-40px;top:0;width:260px;height:360px"></div>
    <div class="brand" style="left:20px;top:175px;font-size:28px">
      <span class="brand-mark" style="width:14px;height:14px"></span>
      <span class="brand-name">Voyara<br>Travel</span>
    </div>
  </section>
  <p class="panel-label" style="left:948px;top:423px">BACK (OPTION 2)</p>

  <section class="panel" style="left:32px;top:453px;width:500px;height:342px">
    <svg class="waves" viewBox="0 0 500 190" preserveAspectRatio="none" aria-hidden="true">
      <path d="M0 80 C130 30 270 140 500 60 L500 190 L0 190Z" fill="rgba(255,255,255,.25)"/>
      <path d="M0 130 C150 80 300 170 500 110" stroke="rgba(255,255,255,.6)" stroke-width="3" fill="none"/>
    </svg>
    <div class="brand" style="left:188px;top:100px;font-size:32px">
      <span class="brand-mark" style="width:16px;height:16px"></span>
      <span class="brand-name">Voyara<br>Travel</span>
    </div>
    <div class="contact" style="left:150px;top:270px;width:200px">
      <span class="pill">555-014-2238</span><br><span class="pill">hello@voyaratravel.com</span><br><span class="web-pill">VoyaraTravel.com</span>
    </div>
  </section>
  <p class="panel-label" style="left:32px;top:809px">OPTION !</p>

  <section class="panel" style="left:553px;top:453px;width:501px;height:342px">
    <svg class="waves" viewBox="0 0 500 190" preserveAspectRatio="none" aria-hidden="true">
      <path d="M0 80 C130 30 270 140 500 60 L500 190 L0 190Z" fill="rgba(255,255,255,.25)"/>
      <path d="M0 130 C150 80 300 170 500 110" stroke="rgba(255,255,255,.6)" stroke-width="3" fill="none"/>
    </svg>
    <div class="faint-globe" role="img" aria-label="Faint wireframe globe decoration" style="left:118px;top:25px;width:290px;height:290px"></div>
    <div class="brand" style="left:190px;top:125px;font-size:32px">
      <span class="brand-mark" style="width:16px;height:16px"></span>
      <span class="brand-name">Voyara<br>Travel</span>
    </div>
  </section>
  <p class="panel-label" style="left:553px;top:801px">OPTION 2</p>

</main>
</body>
</html>
```